GLOW ON THE AVENUE WEBSITE

I have a website www.glowontheavenue.org , need information from that jazzed up. wanted page to be fun & funky .

Target Market(s)

18 to 35yrs guys & girls

Requirements
Must have
• use all photos on website, need to attached my brochure for printing

```html
<!DOCTYPE html>
<html lang="en">
<head>
<meta charset="utf-8">
<title>Glow on the Avenue</title>
<link rel="stylesheet" href="https://fonts.googleapis.com/css2?family=Marcellus+SC&family=Questrial&family=Open+Sans:ital,wght@0,400;0,700;1,700&display=swap">
<style>
:root{
  --pink:#d4187f;
  --pink-soft:#e0609a;
  --ink:#333;
  --grey-text:#555;
  --header-bg:#eeeeec;
  --page-bg:#f4f4f4;
  --footer-top:#3a3a3a;
  --footer-bottom:#1a1a1a;
  --blue:#1d5a8a;
  --green:#3f7a10;
  --amber:#a8650a;
}
*{box-sizing:border-box;margin:0;padding:0}
html,body{width:1185px;height:1200px;overflow:hidden}
body{position:relative;background:var(--page-bg);font-family:"Open Sans",sans-serif;color:var(--ink)}
.top-rule{position:absolute;left:0;top:0;width:1185px;height:5px;background:var(--pink)}
.site-header{position:absolute;left:0;top:5px;width:1185px;height:96px;background:var(--header-bg);border-bottom:2px solid #ddd;box-shadow:0 2px 4px rgba(0,0,0,.08)}
.brand{position:absolute;left:106px;top:30px;font-family:"Questrial",sans-serif;color:var(--pink);font-size:34px;letter-spacing:1px}
.social{position:absolute;left:895px;top:57px;display:flex;gap:14px}
.social span{width:34px;height:34px;border-radius:50%;display:block}
.page-body{position:absolute;left:0;top:103px;width:1185px;height:997px;background:radial-gradient(ellipse at 90% 40%,#e8e8e8,transparent 60%),linear-gradient(#fafafa,#f2f2f2)}
.hero{position:absolute;left:100px;top:120px;width:985px;height:449px;background:#fff;box-shadow:0 10px 18px -8px rgba(0,0,0,.25)}
.hero-photo{position:absolute;left:14px;top:12px;width:958px;height:424px;background:linear-gradient(120deg,#fbf3ee 0%,#e8b89a 30%,#c98a68 55%,#e6b597 75%,#f9f1ec 100%)}
.hero-title{position:absolute;left:127px;top:217px;width:696px;height:64px;background:linear-gradient(90deg,rgba(226,110,170,.95),rgba(214,80,140,.92));color:#fff;font-family:"Marcellus SC",serif;font-size:34px;padding:10px 14px;letter-spacing:1px}
.hero-points{position:absolute;left:209px;top:281px;width:696px;height:99px;background:rgba(100,78,66,.72);list-style:none;padding:8px 18px;color:#fff;font-family:"Questrial",sans-serif;font-size:15px;letter-spacing:.4px}
.hero-points li{display:flex;align-items:center;gap:14px;height:29px}
.sidebar{position:absolute;left:102px;top:640px;width:272px;height:418px;background:linear-gradient(90deg,#fff,#efefef);border:2px solid #e2e2e2;border-radius:10px;box-shadow:0 1px 4px rgba(0,0,0,.12);padding:16px 22px 0 14px}
.sidebar ul{list-style:none}
.sidebar li{height:32px;display:flex;align-items:center;gap:14px;border-bottom:1px dotted #ccc;font-family:"Questrial",sans-serif;font-size:15px;color:var(--grey-text)}
.sidebar li:last-child{border-bottom:none}
.welcome-title{position:absolute;left:400px;top:645px;font-family:"Marcellus SC",serif;font-size:22px;color:var(--ink);letter-spacing:1px}
.welcome-title em{font-style:normal;color:var(--pink-soft)}
.welcome-figure{position:absolute;left:404px;top:680px;width:125px;height:190px;border-radius:40% 40% 30% 30%;background:radial-gradient(ellipse at 50% 40%,#c9906a,#e8cdbb 60%,transparent 75%)}
.welcome-copy{position:absolute;left:542px;top:703px;width:531px;font-size:10.5px;line-height:18px;text-align:justify;color:#333}
.welcome-copy p+p{margin-top:18px}
.feature{position:absolute;top:915px;width:202px;height:140px;border-radius:12px;padding:10px 16px;border:2px solid}
.feature h3{font-family:"Marcellus SC",serif;font-weight:400;font-size:20px;letter-spacing:1px}
.feature p{font-size:10.5px;line-height:18px;margin-top:10px;text-align:justify;color:#333}
.feature .more{position:absolute;right:20px;bottom:10px;font-size:10px;color:#555}
.feature-brow{left:406px;background:linear-gradient(#fff,#cde8fa);border-color:#cfe6f6}
.feature-brow h3{color:var(--blue)}
.feature-hand{left:630px;background:linear-gradient(#fff,#def7c8);border-color:#dcf1c6}
.feature-hand h3{color:var(--green)}
.feature-facial{left:854px;background:linear-gradient(#fff,#fcebc6);border-color:#f7e3bd}
.feature-facial h3{color:var(--amber)}
.site-footer{position:absolute;left:0;top:1100px;width:1185px;height:100px;background:linear-gradient(var(--footer-top),var(--footer-bottom));color:#ccc;text-align:center;font-family:"Questrial",sans-serif;font-size:11px;letter-spacing:.4px}
.footer-nav{margin-top:27px}
.copyright{margin-top:22px}
</style>
</head>
<body>
<div class="top-rule"></div>
<header class="site-header">
  <div class="brand">Glow on the Avenue</div>
  <div class="social" aria-label="Social links">
    <span style="background:#2b4a8c" aria-label="Social network"></span>
    <span style="background:#c9c9c9" aria-label="Video channel"></span>
    <span style="background:#45b6e6" aria-label="Microblog"></span>
    <span style="background:#f26a1b" aria-label="News feed"></span>
  </div>
</header>
<main class="page-body"></main>
<section class="hero">
  <div class="hero-photo" role="img" aria-label="Photo of smooth bare legs after waxing"></div>
</section>
<h1 class="hero-title">The New Lavender Silk Wax</h1>
<ul class="hero-points">
  <li><svg width="14" height="12" viewBox="0 0 14 12"><path d="M1 6l4 4 8-9" fill="none" stroke="#fff" stroke-width="2.5"/></svg>The perfect strip wax and hot wax hybrid with an even lower melting temperature.</li>
  <li><svg width="14" height="12" viewBox="0 0 14 12"><path d="M1 6l4 4 8-9" fill="none" stroke="#fff" stroke-width="2.5"/></svg>A top notch performance wax with the strength and pliability.</li>
  <li><svg width="14" height="12" viewBox="0 0 14 12"><path d="M1 6l4 4 8-9" fill="none" stroke="#fff" stroke-width="2.5"/></svg>Fantastic for all intimate waxing from facial waxing to Brazilians.</li>
</ul>
<nav class="sidebar">
  <ul>
    <li><svg width="14" height="12" viewBox="0 0 14 12"><rect x="0.5" y="3" width="9" height="8" fill="none" stroke="#bbb"/><path d="M2 6l3 3 8-8" fill="none" stroke="var(--pink)" stroke-width="2.2"/></svg>Wecome</li>
    <li><svg width="14" height="12" viewBox="0 0 14 12"><rect x="0.5" y="3" width="9" height="8" fill="none" stroke="#bbb"/><path d="M2 6l3 3 8-8" fill="none" stroke="var(--pink)" stroke-width="2.2"/></svg>Waxing</li>
    <li><svg width="14" height="12" viewBox="0 0 14 12"><rect x="0.5" y="3" width="9" height="8" fill="none" stroke="#bbb"/><path d="M2 6l3 3 8-8" fill="none" stroke="var(--pink)" stroke-width="2.2"/></svg>City brow bar</li>
    <li><svg width="14" height="12" viewBox="0 0 14 12"><rect x="0.5" y="3" width="9" height="8" fill="none" stroke="#bbb"/><path d="M2 6l3 3 8-8" fill="none" stroke="var(--pink)" stroke-width="2.2"/></svg>Eyes incl. Lash extensions</li>
    <li><svg width="14" height="12" viewBox="0 0 14 12"><rect x="0.5" y="3" width="9" height="8" fill="none" stroke="#bbb"/><path d="M2 6l3 3 8-8" fill="none" stroke="var(--pink)" stroke-width="2.2"/></svg>Tanning</li>
    <li><svg width="14" height="12" viewBox="0 0 14 12"><rect x="0.5" y="3" width="9" height="8" fill="none" stroke="#bbb"/><path d="M2 6l3 3 8-8" fill="none" stroke="var(--pink)" stroke-width="2.2"/></svg>Hand &amp; Feet</li>
    <li><svg width="14" height="12" viewBox="0 0 14 12"><rect x="0.5" y="3" width="9" height="8" fill="none" stroke="#bbb"/><path d="M2 6l3 3 8-8" fill="none" stroke="var(--pink)" stroke-width="2.2"/></svg>Facials &amp; Massage</li>
    <li><svg width="14" height="12" viewBox="0 0 14 12"><rect x="0.5" y="3" width="9" height="8" fill="none" stroke="#bbb"/><path d="M2 6l3 3 8-8" fill="none" stroke="var(--pink)" stroke-width="2.2"/></svg>Makeup</li>
    <li><svg width="14" height="12" viewBox="0 0 14 12"><rect x="0.5" y="3" width="9" height="8" fill="none" stroke="#bbb"/><path d="M2 6l3 3 8-8" fill="none" stroke="var(--pink)" stroke-width="2.2"/></svg>Specials</li>
    <li><svg width="14" height="12" viewBox="0 0 14 12"><rect x="0.5" y="3" width="9" height="8" fill="none" stroke="#bbb"/><path d="M2 6l3 3 8-8" fill="none" stroke="var(--pink)" stroke-width="2.2"/></svg>Products</li>
    <li><svg width="14" height="12" viewBox="0 0 14 12"><rect x="0.5" y="3" width="9" height="8" fill="none" stroke="#bbb"/><path d="M2 6l3 3 8-8" fill="none" stroke="var(--pink)" stroke-width="2.2"/></svg>Blog</li>
    <li><svg width="14" height="12" viewBox="0 0 14 12"><rect x="0.5" y="3" width="9" height="8" fill="none" stroke="#bbb"/><path d="M2 6l3 3 8-8" fill="none" stroke="var(--pink)" stroke-width="2.2"/></svg>Contact Us</li>
  </ul>
</nav>
<h2 class="welcome-title"><em>Welcome To</em> Glow on the Avenue</h2>
<div class="welcome-figure" role="img" aria-label="Photo of a seated woman wrapped in a white towel, seen from behind"></div>
<div class="welcome-copy">
  <p><strong><i>Lorem Ipsum is simply dummy text of the printing and typesetting industry. Lorem Ipsum has been the industry's standard dummy</i></strong> text ever since the 1500s, when an unknown printer took a galley of type and scrambled it to make a type specimen book. It has survived not only five centuries, but also the leap into electronic typesetting, remaining essentially unchanged. It was popularised in</p>
  <p>The 1960s with the release of Typeset Press sheets containing Lorem Ipsum passages, and more recently release of Typeset Press sheets containing Lorem Ipsum with desktop publishing software like Folio LayoutDesk including versions of Lorem Ipsum.</p>
</div>
<article class="feature feature-brow">
  <h3>City Brow Bar</h3>
  <p>Nulla pharetra enim vel lacus cursus in placerat lorem rutrum cursus in placerat</p>
  <span class="more">more details &#9656;</span>
</article>
<article class="feature feature-hand">
  <h3>Hand Feet</h3>
  <p>Nulla pharetra enim vel lacus cursus in placerat lorem rutrum cursus in placerat</p>
  <span class="more">more details &#9656;</span>
</article>
<article class="feature feature-facial">
  <h3>Facials &amp; Massage</h3>
  <p>Nulla pharetra enim vel lacus cursus in placerat lorem rutrum cursus in placerat</p>
  <span class="more">more details &#9656;</span>
</article>
<footer class="site-footer">
  <p class="footer-nav">Welcome | Waxing | City brow bar | Eyes incl. Lash extensions | Tanning | Hands &amp; Feet | Facials &amp; Massage | Makeup | Specials | Products | Blog | Contact Us</p>
  <p class="copyright">&copy;2010 SalonPages.net. All Rights Reserved.</p>
</footer>
</body>
</html>
```